Website for Torvel Capital - investment banking firm

We have a corporate identity (thanks to Ranjita/41238) and want to extend that into a website design.  See the attached zipped files.
We have software folks in-house to do the coding.
See the attached Project Brief & Notes for more details.  Don't worry about the actual text - lorem ipsum will be fine.
The server will be Apache.
Thank you!
Desmond

```html
<!DOCTYPE html>
<html lang="en">
<head>
<meta charset="utf-8">
<title>Torvel Capital</title>
<link href="https://fonts.googleapis.com/css2?family=Roboto+Condensed:wght@400;700&family=Arimo:wght@400;700&family=Open+Sans:wght@600&display=swap" rel="stylesheet">
<style>
:root{
  --brand:#1d4c9a;
  --brand-dark:#0f2f6b;
  --nav-top:#2a79d2;
  --nav-bottom:#1555ad;
  --text:#6d6d6d;
  --heading:#1d4c9a;
  --rule:#d9d9d9;
  --btn:#555a61;
  --footer:#222426;
  --footer-bottom:#141516;
  --link:#3aa6e0;
}
*{margin:0;padding:0;box-sizing:border-box}
html,body{width:1200px;height:2423px;overflow:hidden;background:#fff}
body{position:relative;font-family:"Arimo",Arial,sans-serif;color:var(--text);font-size:11.5px;line-height:22px}
.abs{position:absolute}
h2,h3,h4{font-family:"Roboto Condensed",Arial,sans-serif;font-weight:400;color:var(--heading)}
h2{font-size:21px;line-height:26px}
h4{font-size:14px;line-height:18px}

.topline{top:0;left:0;width:1200px;height:4px;background:var(--brand-dark)}
.logo{top:32px;left:130px;display:flex;align-items:center;gap:14px}
.logo-mark{width:40px;height:40px;border-radius:50%;background:var(--brand)}
.logo-name{font-family:"Roboto Condensed",Arial,sans-serif;font-weight:400;font-size:30px;line-height:40px;color:var(--brand)}
.search{top:35px;left:738px;width:329px;height:44px;border:1px solid #c9c9c9;font-size:10px;color:#666;padding:13px 16px;line-height:16px}
.search svg{position:absolute;right:16px;top:13px}

.nav{top:108px;left:0;width:1200px;height:55px;background:linear-gradient(var(--nav-top),var(--nav-bottom));display:flex;padding-left:132px}
.nav a{font-family:"Roboto Condensed",Arial,sans-serif;font-size:15px;color:#fff;text-decoration:none;line-height:55px;text-align:center}
.nav a.active{background:var(--brand-dark)}

.hero{top:163px;left:0;width:1200px;height:512px;background:linear-gradient(180deg,#9a9a9a 0%,#b8b8b8 55%,#8d8d8d 100%)}
.hero-arrow{top:395px}

.welcome{top:700px;left:170px;width:860px;text-align:center}
.welcome h2{font-size:22px;margin-bottom:16px}
.welcome p{font-size:11px;line-height:28px}
.rule{left:132px;width:934px;height:1px;background:var(--rule)}

.services-title{top:896px;left:132px}
.pager{display:flex;gap:8px;color:#aaa}
.service{top:950px;width:198px}
.service .photo{height:142px}
.service h4{font-family:"Arimo",Arial,sans-serif;font-size:12px;margin:20px 0 8px}
.service p{font-size:10.5px}

.searches{top:896px;left:782px;width:284px}
.searches h2{margin-bottom:14px}
.search-item{border-bottom:1px solid var(--rule);padding:8px 0 4px}
.search-item h4{font-size:15px;margin-bottom:6px}
.search-item p{font-size:11px}

.col-title{top:1300px}
.process{left:132px;width:268px}
.process p{font-size:11px}
.process h3{font-size:16px;font-weight:700;margin:20px 0 10px}
.ticks{list-style:none}
.ticks li{display:flex;align-items:center;gap:10px;font-size:11px;line-height:29px}

.btn{width:208px;height:45px;background:var(--btn);border:1px solid #3d4146;color:#fff;font-family:"Roboto Condensed",Arial,sans-serif;font-size:16px;text-align:center;line-height:43px}

.team{left:452px;width:296px}
.member{display:flex;gap:20px;padding:0 0 15px;border-bottom:1px solid var(--rule);margin-bottom:14px}
.member:last-child{border:none}
.member .photo{width:84px;height:73px;flex:none}
.member h4{font-family:"Arimo",Arial,sans-serif;font-size:12px;margin-bottom:8px}
.member p{font-size:11px}

.about{left:772px;width:294px}

.quote-band{top:1712px;left:0;width:1200px;height:124px;background:linear-gradient(#fff,#efefef);border-top:1px solid #eee;border-bottom:1px solid #e5e5e5}
.quote{top:1740px;left:160px;width:880px;font-size:11px;line-height:40px}
.quote-mark{font-family:Georgia,serif;font-size:38px;color:#555}

.clients-title{top:1860px;left:132px;font-family:"Open Sans",Arial,sans-serif;font-weight:600;font-size:21px;color:var(--brand)}
.clients{top:1906px;left:136px;display:flex;gap:18px}
.client{width:172px;height:77px;border:1px solid #e6e6e6;display:flex;align-items:center;justify-content:center;gap:8px;font-family:"Arimo",Arial,sans-serif;font-size:17px;color:#9a9a9a}
.client i{width:12px;height:12px;border-radius:50%;background:#b5b5b5}

.footer{top:2030px;left:0;width:1200px;height:333px;background:var(--footer)}
.footer h3{font-family:"Roboto Condensed",Arial,sans-serif;color:#fff;font-size:19px;margin-bottom:24px}
.footer p,.footer li{color:#fff;font-size:11px}
.tweet{margin-bottom:22px}
.tweet span{color:var(--link)}
.field{width:263px;height:42px;border:1px solid #fff;color:#fff;font-size:11px;padding:0 14px;line-height:40px;margin-top:24px}
.submit{margin-top:24px;width:112px;height:40px;background:var(--brand);border:1px solid #fff;color:#fff;font-size:14px;text-align:center;line-height:38px}
.map{top:2062px;left:818px;width:250px;height:160px;background:radial-gradient(ellipse,#34373a,#222426 70%)}
.contact-row{display:flex;gap:14px;margin-bottom:14px;line-height:18px}
.contact-row svg{flex:none;margin-top:2px}

.bottom{top:2363px;left:0;width:1200px;height:60px;background:var(--footer-bottom);color:#fff;font-size:11px;text-align:center;line-height:60px}
</style>
</head>
<body>
<div class="abs topline"></div>
<header>
  <div class="abs logo"><span class="logo-mark"></span><span class="logo-name">Torvel Capital</span></div>
  <div class="abs search">Enter Any Keyword.....
    <svg width="16" height="16" viewBox="0 0 16 16"><circle cx="6" cy="6" r="4.5" fill="none" stroke="#888" stroke-width="1.5"/><line x1="9.5" y1="9.5" x2="14" y2="14" stroke="#888" stroke-width="2"/></svg>
  </div>
  <nav class="abs nav">
    <a class="active" href="#" style="width:108px">Home</a>
    <a href="#" style="width:128px">About</a>
    <a href="#" style="width:120px">Services</a>
    <a href="#" style="width:190px">Current Engagements</a>
    <a href="#" style="width:210px">Completed Transactions</a>
    <a href="#" style="width:168px">Contact Us</a>
  </nav>
</header>

<section class="abs hero" role="img" aria-label="Business people assembling a wall of large white puzzle pieces on a grey backdrop"></section>
<svg class="abs hero-arrow" style="left:55px" width="52" height="52" viewBox="0 0 52 52"><circle cx="26" cy="26" r="23" fill="none" stroke="#fff" stroke-width="3"/><path d="M32 14 L18 26 L32 38 Z" fill="#fff"/></svg>
<svg class="abs hero-arrow" style="left:1097px" width="52" height="52" viewBox="0 0 52 52"><circle cx="26" cy="26" r="23" fill="none" stroke="#fff" stroke-width="3"/><path d="M20 14 L34 26 L20 38 Z" fill="#fff"/></svg>

<section class="abs welcome">
  <h2>Welcome to Our Company</h2>
  <p>Torvel Capital is an independent investment bank working for buyers in a number of industries. We utilize exceptional technology in finding companies that meet buyer's search criteria. We will not waste a buyer's time, a seller's time or our own time.Torvel Capital is an independent investment bank working for buyers in a number of industries. We utilize exceptional technology in finding companies that meet buyer's search criteria.</p>
</section>
<div class="abs rule" style="top:862px"></div>

<h2 class="abs services-title">Our Services</h2>
<div class="abs pager" style="top:898px;left:726px;font-size:12px">‹ ›</div>
<article class="abs service" style="left:132px">
  <div class="photo" role="img" aria-label="Businessman in a suit touching a glowing digital interface" style="background:linear-gradient(135deg,#1d2a3c,#5c7fa6,#243040)"></div>
  <h4>Buy-SideAcquisitions</h4>
  <p>We've can give buyers access to sophis-ticated software tools that enable your target requirements to automatically create a list service lines....</p>
</article>
<article class="abs service" style="left:344px">
  <div class="photo" role="img" aria-label="Hands holding a tablet showing charts beside a coffee cup" style="background:linear-gradient(135deg,#f1f1f1,#cfcfcf,#efe8e0)"></div>
  <h4>Recapitalizations&amp; Growth Partners</h4>
  <p>We've can give buyers access to sophis-ticated software tools that enable your target requirements to automatically create a list service lines....</p>
</article>
<article class="abs service" style="left:556px">
  <div class="photo" role="img" aria-label="Business team gathered around a laptop in a meeting" style="background:linear-gradient(135deg,#e6e6e6,#8e8a86,#d9d4ce)"></div>
  <h4>Sell-SideTransactions</h4>
  <p>We've can give buyers access to sophis-ticated software tools that enable your target requirements to automatically create a list service lines....</p>
</article>

<aside class="abs searches">
  <h2>M&amp;A Searches</h2>
  <div class="search-item"><h4>Current Engagement</h4><p>We've can give buyers access to sophisticated software tools that enable your target create a list service lines....</p></div>
  <div class="search-item" style="padding-top:12px"><h4>Completed Transaction</h4><p>We've can give buyers access to sophisticated software tools that enable your target create a list service lines....</p></div>
  <div class="search-item" style="padding-top:14px"><h4>Regulatory Compliances</h4><p>We've can give buyers access to sophisticated software tools that enable your target create a list service lines....</p></div>
</aside>
<div class="abs rule" style="top:1269px"></div>

<section class="abs col-title process">
  <h2 style="margin-bottom:14px">Our Process</h2>
  <p>Once we have your acquisition parameters, we feed these into our software to create an initial target list. these into our software to create an initial target list. holder structure.....</p>
  <h3>Torvel Capital's technology :</h3>
  <ul class="ticks">
    <li><svg width="14" height="12" viewBox="0 0 14 12"><path d="M1 6 L5 10 L13 1" fill="none" stroke="#7cb32f" stroke-width="2.5"/></svg>Technology</li>
    <li><svg width="14" height="12" viewBox="0 0 14 12"><path d="M1 6 L5 10 L13 1" fill="none" stroke="#7cb32f" stroke-width="2.5"/></svg>Process</li>
    <li><svg width="14" height="12" viewBox="0 0 14 12"><path d="M1 6 L5 10 L13 1" fill="none" stroke="#7cb32f" stroke-width="2.5"/></svg>Professional discipline</li>
  </ul>
</section>
<div class="abs btn" style="top:1616px;left:132px">Click Here For More Info</div>

<section class="abs col-title team">
  <h2 style="margin-bottom:14px">Our Teams</h2>
  <div class="member"><div class="photo" role="img" aria-label="Portrait of a smiling team member" style="background:linear-gradient(135deg,#f3f3f3,#b89a82,#eee)"></div><div><h4>Our team is made a diversified</h4><p>Torvel Capital's team of bankers and advisors enced professionals.....</p></div></div>
  <div class="member"><div class="photo" role="img" aria-label="Group portrait of the advisory team" style="background:linear-gradient(135deg,#eee,#9a8a80,#e5e5e5)"></div><div><h4>Our team is made a diversified</h4><p>Torvel Capital's team of bankers and advisors enced professionals.....</p></div></div>
  <div class="member"><div class="photo" role="img" aria-label="Group portrait of the banking team" style="background:linear-gradient(135deg,#eee,#8f8a88,#e2e2e2)"></div><div><h4>Our team is made a diversified</h4><p>Torvel Capital's team of bankers and advisors enced professionals.....</p></div></div>
</section>

<section class="abs col-title about">
  <h2 style="margin-bottom:14px">About Torvel Capital</h2>
  <div role="img" aria-label="Two colleagues reviewing financial charts in a bright office" style="height:158px;background:linear-gradient(135deg,#f2f4f6,#9fb0c2,#e7eaee)"></div>
  <p style="margin-top:12px;font-size:11px">When our software has identified a qualified list, Torvel will reach out to prospective sellers. We will gather basic seller to reach out directly to the buyer......</p>
</section>
<div class="abs btn" style="top:1616px;left:777px">Click Here For More Info</div>

<div class="abs quote-band"></div>
<blockquote class="abs quote"><span class="quote-mark" style="position:absolute;left:0;top:-14px">“</span><span style="padding-left:28px;display:block">Torvel Capital is currently working on several searches in a wide variety of industries and fields. All of our searches have the following common themes:successful company. Buyers are buying the people who have built the company. ......... <span class="quote-mark" style="vertical-align:-18px">”</span></span></blockquote>

<h2 class="abs clients-title">Clients</h2>
<div class="abs pager" style="top:1866px;left:1044px;font-size:12px">‹ ›</div>
<div class="abs clients">
  <div class="client"><i></i>Larkfield</div>
  <div class="client">Quillmark</div>
  <div class="client">Varneo</div>
  <div class="client"><i></i>Ostrel</div>
  <div class="client"><i></i>Nordvane</div>
</div>

<footer class="abs footer">
  <div class="abs map" role="img" aria-label="Faint world map"></div>
  <div class="abs" style="top:16px;left:157px;width:260px">
    <h3>Recent Twetter</h3>
    <p class="tweet">Check out this great #templatehall item 'Civic Ledger - <span>HTML Template' http://t.co/kR4wzLm8Qe 5th Dec 2013</span></p>
    <p class="tweet" style="margin-top:28px">Check out this great #templatehall item 'Civic Ledger - <span>HTML Template' http://t.co/kR4wzLm8Qe 5th Dec 2013</span></p>
  </div>
  <div class="abs" style="top:16px;left:485px;width:290px">
    <h3>News Letters</h3>
    <p>consectetur adipisicing elit, sed do eiusmod tempor incididunt ut labore et dolore magna aliqua.</p>
    <div class="field">Enter Your Id :</div>
    <div class="field">Enter Your Id :</div>
    <div class="submit">SUBMIT</div>
  </div>
  <div class="abs" style="top:12px;left:833px;width:240px">
    <h3>Contact Us</h3>
    <div class="contact-row"><svg width="12" height="16" viewBox="0 0 12 16"><path d="M6 0 A6 6 0 0 1 12 6 C12 10 6 16 6 16 C6 16 0 10 0 6 A6 6 0 0 1 6 0 Z" fill="#999"/><circle cx="6" cy="6" r="2" fill="#222"/></svg><p>Hong Kong: Suite 1804 Harbourline Tower 112 - 118 Marlow Road East Eastbay, Hong Kong</p></div>
    <div class="contact-row"><svg width="12" height="16" viewBox="0 0 12 16"><path d="M2 1 L5 1 L6 5 L4 6 C5 9 6 10 8 11 L9 9 L12 11 L11 15 C5 15 0 9 1 2 Z" fill="#999"/></svg><p>Phone: 604-555-0148<br>Fax: 469-555-0172</p></div>
    <div class="contact-row"><svg width="14" height="10" viewBox="0 0 14 10"><rect width="14" height="10" fill="#999"/><path d="M0 0 L7 6 L14 0" fill="none" stroke="#222"/></svg><p>info@torvelcapital.com</p></div>
  </div>
</footer>
<div class="abs bottom">CopyRight 2014 Torvel Capital.All Right Reserved.</div>
</body>
</html>
```